Surveillance Sign

Design sign and stickers with a line drawing of the camera.

Industry/Entity Type

Camera

Requirements
Nice to have
• I like this design: http://www.varnotek.com/cctv-camera-warning-signs-decals/camera-surveillance-sign

```html
<!DOCTYPE html>
<html lang="en">
<head>
<meta charset="utf-8">
<title>Surveillance Sign</title>
<link rel="stylesheet" href="https://fonts.googleapis.com/css2?family=Alfa+Slab+One&family=Montserrat:wght@800&display=swap">
<style>
  :root {
    --backdrop: #000000;
    --sign-red-dark: #bd1e24;
    --sign-red: #e52330;
    --sign-white: #ffffff;
    --sign-yellow: #fff200;
    --ink: #111111;
    --camera-light: #d9d9d9;
    --camera-dark: #5a5a5a;
  }
  html, body {
    margin: 0;
    padding: 0;
    width: 1161px;
    height: 1200px;
    overflow: hidden;
    background: var(--backdrop);
  }
  .sign {
    position: absolute;
    left: 210px;
    top: 129px;
    width: 740px;
    height: 941px;
    background: var(--sign-white);
    overflow: hidden;
  }
  .sign__header-field {
    position: absolute;
    left: 0;
    top: 0;
    width: 740px;
    height: 470px;
  }
  .sign__kicker {
    position: absolute;
    left: 0;
    top: 38px;
    width: 100%;
    margin: 0;
    text-align: center;
    font-family: "Alfa Slab One", serif;
    font-weight: 400;
    font-size: 66px;
    line-height: 1;
    letter-spacing: 1px;
    color: var(--sign-yellow);
  }
  .sign__camera-art {
    position: absolute;
    left: 22px;
    top: 107px;
    width: 455px;
    height: 340px;
    border-radius: 40px 120px 60px 60px;
    background: radial-gradient(ellipse at 55% 45%, var(--camera-light) 0%, #a8a8a8 45%, var(--camera-dark) 100%);
  }
  .sign__headline {
    position: absolute;
    left: 34px;
    top: 464px;
    margin: 0;
    font-family: "Alfa Slab One", serif;
    font-weight: 400;
    font-size: 76px;
    line-height: 68px;
    letter-spacing: -0.5px;
    color: var(--ink);
  }
  .sign__headline-accent {
    color: var(--sign-red);
  }
  .sign__notice {
    position: absolute;
    left: 34px;
    top: 746px;
    width: 690px;
    margin: 0;
    font-family: "Montserrat", sans-serif;
    font-weight: 800;
    font-size: 27.5px;
    line-height: 32px;
    letter-spacing: -0.4px;
    color: var(--ink);
  }
  .sign__footer {
    position: absolute;
    left: 0;
    top: 883px;
    width: 740px;
    height: 58px;
    background: var(--sign-red);
    display: flex;
    align-items: center;
    justify-content: center;
  }
  .sign__url {
    font-family: "Montserrat", sans-serif;
    font-weight: 800;
    font-size: 27px;
    letter-spacing: 3px;
    color: var(--sign-yellow);
  }
</style>
</head>
<body>
  <main class="sign">
    <svg class="sign__header-field" viewBox="0 0 740 470" aria-hidden="true">
      <polygon points="0,0 740,0 740,467 0,263" fill="var(--sign-red-dark)"/>
    </svg>
    <p class="sign__kicker">SURVEILLANCE</p>
    <div class="sign__camera-art" role="img" aria-label="Illustration of a wall-mounted bullet CCTV security camera with infrared lens ring"></div>
    <h1 class="sign__headline">THIS PROPERTY<br>PROTECTED BY<br><span class="sign__headline-accent">CCTV SECURITY<br>CAMERAS</span></h1>
    <p class="sign__notice">FOR YOUR PERSONAL PROTECTION ALL<br>ACTIVITIES ARE RECORDED ON DIGITAL MEDIA<br>TO AID IN THE PROSECUTION OF ANY CRIME<br>COMMITTED ON THIS PROPERTY.</p>
    <footer class="sign__footer">
      <span class="sign__url">www.varnotek.com</span>
    </footer>
  </main>
</body>
</html>
```